2015 Larkmoor College Smoke-free poster

We need a design of an A3 poster that we will print in-house on a good quality photocopier. The poster is only to be used for students and staff at our College, to remind them that we are now smoke-free. We need the poster designed to meet our style guide rules. We will need the final artwork as a high res PDF, as well as the working files (whether InDesign, etc.).

Target Market(s)

Staff and students at university level

Industry/Entity Type

College

Font styles to use
Sans Serif

Requirements
Must have
• The Larkmoor College logo
• The Larkmoor College red colour

```html
<!DOCTYPE html>
<html lang="en">
<head>
<meta charset="utf-8">
<title>Larkmoor College – Smoke-free poster</title>
<link href="https://fonts.googleapis.com/css2?family=Barlow:wght@300;400;600;700&display=swap" rel="stylesheet">
<style>
  :root {
    --college-red: #ad1f2e;
    --deep-red: #7e1a21;
    --ink: #1c1c1c;
    --grey: #7a7a7a;
    --paper: #ffffff;
  }
  html, body { margin: 0; padding: 0; overflow: hidden; background: var(--paper); }
  .poster {
    position: relative;
    width: 848px;
    height: 1200px;
    overflow: hidden;
    background: var(--paper);
    font-family: "Barlow", Arial, sans-serif;
  }
  .artwork { position: absolute; inset: 0; }
  .headline {
    font-family: "Barlow", Arial, sans-serif;
    font-weight: 700;
    font-size: 46px;
    fill: var(--ink);
    letter-spacing: 1px;
  }
  .commitment {
    font-family: "Barlow", Arial, sans-serif;
    font-weight: 400;
    font-size: 13.5px;
    fill: var(--college-red);
  }
  .info {
    position: absolute;
    left: 33px;
    padding-left: 22px;
  }
  .info h2 {
    margin: 0;
    font-size: 23px;
    font-weight: 700;
    line-height: 1.15;
  }
  .info p {
    margin: 2px 0 0;
    font-size: 18.5px;
    font-weight: 300;
    line-height: 1.27;
  }
  .info .cig {
    position: absolute;
    left: 0;
    top: 4px;
  }
  .info--light { top: 888px; width: 345px; }
  .info--light h2, .info--light p { color: var(--college-red); }
  .info--quit { top: 1010px; width: 370px; }
  .info--quit h2, .info--quit p { color: var(--grey); }
  .web-address {
    position: absolute;
    left: 33px;
    top: 1124px;
    margin: 0;
    font-size: 22px;
    font-weight: 600;
    color: var(--college-red);
    letter-spacing: 0.3px;
  }
  .college-mark {
    position: absolute;
    left: 547px;
    top: 1105px;
    display: flex;
    align-items: center;
    gap: 12px;
  }
  .college-mark .square {
    width: 44px;
    height: 44px;
    background: var(--college-red);
  }
  .college-mark .name {
    font-size: 22px;
    font-weight: 700;
    color: var(--ink);
    text-transform: uppercase;
    letter-spacing: 0.3px;
  }
</style>
</head>
<body>
<main class="poster">
  <svg class="artwork" width="848" height="1200" viewBox="0 0 848 1200">
    <defs>
      <radialGradient id="smoke-tone" cx="0.4" cy="0.3" r="0.7">
        <stop offset="0" stop-color="#bdbdbd"/>
        <stop offset="0.5" stop-color="#e2e2e2"/>
        <stop offset="1" stop-color="#ffffff"/>
      </radialGradient>
    </defs>
    <rect class="smoke" x="0" y="0" width="848" height="640" fill="url(#smoke-tone)" role="img" aria-label="Soft grey wisps of rising smoke"/>
    <polygon class="banner-outer" points="25,650 848,232 848,1035" fill="var(--college-red)"/>
    <polygon class="banner-inner" points="255,650 848,350 848,945" fill="var(--deep-red)"/>
    <text class="headline" x="68" y="592" transform="rotate(-26.9 68 592)" textLength="822" lengthAdjust="spacingAndGlyphs">WELCOME TO A SMOKE-FREE LARKMOOR</text>
    <text class="commitment" x="48" y="684" transform="rotate(26.6 48 684)" textLength="835" lengthAdjust="spacingAndGlyphs">It’s part of our commitment to providing a safe and healthy environment for all staff, students, contractors and visitors.</text>
  </svg>

  <section class="info info--light">
    <svg class="cig" width="14" height="82" viewBox="0 0 14 82" aria-hidden="true">
      <rect x="1" y="1" width="12" height="80" fill="none" stroke="var(--college-red)" stroke-width="1.5"/>
      <rect x="1" y="60" width="12" height="21" fill="var(--college-red)"/>
      <line x1="3" y1="5" x2="11" y2="5" stroke="var(--college-red)" stroke-width="1"/>
      <line x1="3" y1="8" x2="11" y2="8" stroke="var(--college-red)" stroke-width="1"/>
    </svg>
    <h2>Looking to light up?</h2>
    <p>For 2015, we’ve installed a designated smoking area in the northern car park on the residential Ashcombe campus.</p>
  </section>

  <section class="info info--quit">
    <svg class="cig" width="14" height="50" viewBox="0 0 14 50" aria-hidden="true">
      <rect x="1" y="0" width="12" height="20" fill="var(--grey)"/>
      <path d="M1 22 h12 v6 l-3 6 h-6 l-3 -6 z" fill="none" stroke="var(--grey)" stroke-width="1.3"/>
    </svg>
    <h2>Looking to quit?</h2>
    <p>We’re here to help. See us for counseling services and information on ways to quit.</p>
  </section>

  <p class="web-address">www.larkmoor.harwood.edu.au/smoke-free</p>

  <div class="college-mark">
    <span class="square" aria-hidden="true"></span>
    <span class="name">Larkmoor College</span>
  </div>
</main>
</body>
</html>
```